Poster design for - Glowing Meadow Festival

To design a dynamic illustrated Glowing Meadow Festival poster.
The dates are: 3-5 July 2020
Location: Tarlow Campsite, Ashcombe, Fernshire
www.glowingmeadow.co.uk

Here is some text about the event to give you an idea. You can take elements from it if you like:

A Gathering of Female Energy to Ignite and Embrace the Power of Woman with Mother Earth.

Target Market(s)

Women festival goers.

Industry/Entity Type

Festival

Colors

Designer to choose colors to be used in the design.

Requirements
Must have
• Glowing Meadow Logo - but this can be altered to look washed out.
• Date, location, website url.
Nice to have
• Earthy, hippy, festival look.

```html
<!DOCTYPE html>
<html lang="en">
<head>
<meta charset="utf-8">
<title>Glowing Meadow Festival – 3–5 July 2020</title>
<link rel="stylesheet" href="https://fonts.googleapis.com/css2?family=Bebas+Neue&family=Barlow:wght@400;600;700&display=swap">
<style>
  :root {
    --frame: #ef572e;
    --paper: #f4f5f6;
    --ink: #0b0b0c;
    --flame-1: #f6861f;
    --flame-2: #e8362a;
    --accent: #e8532b;
    --teal: #5cc6c4;
    --orange: #f38525;
    --coral: #ee6a55;
    --sun: #f2ea5a;
  }
  html, body {
    margin: 0;
    padding: 0;
    width: 1200px;
    height: 1200px;
    overflow: hidden;
    background: var(--frame);
  }
  .canvas {
    position: relative;
    width: 1200px;
    height: 1200px;
    background: var(--frame);
  }
  .poster {
    position: absolute;
    left: 245px;
    top: 67px;
    width: 710px;
    height: 1065px;
    background: var(--paper);
    overflow: hidden;
  }

  /* decorative areas */
  .deco { position: absolute; pointer-events: none; }
  .bunting-left {
    left: -20px; top: -10px; width: 270px; height: 90px;
    transform-origin: left top; transform: translate(0, 150px) rotate(-34deg);
    background: linear-gradient(90deg, rgba(92,198,196,.55), rgba(243,133,37,.55));
    border-radius: 0 0 40px 40px;
  }
  .bunting-right {
    right: -20px; top: -10px; width: 270px; height: 90px;
    transform-origin: right top; transform: translate(0, 150px) rotate(34deg);
    background: linear-gradient(270deg, rgba(92,198,196,.55), rgba(243,133,37,.55));
    border-radius: 0 0 40px 40px;
  }
  .burst { border-radius: 50%; }
  .burst-top {
    left: 390px; top: 20px; width: 230px; height: 230px;
    background: radial-gradient(circle, rgba(238,106,85,.28) 0%, rgba(138,128,200,.18) 45%, rgba(244,245,246,0) 70%);
  }
  .burst-left {
    left: 40px; top: 150px; width: 320px; height: 320px;
    background: radial-gradient(circle, rgba(92,198,196,.3) 0%, rgba(243,133,37,.22) 45%, rgba(244,245,246,0) 70%);
  }
  .burst-mid {
    left: 370px; top: 410px; width: 170px; height: 170px;
    background: radial-gradient(circle, rgba(242,234,90,.3) 0%, rgba(243,133,37,.2) 45%, rgba(244,245,246,0) 70%);
  }
  .burst-low {
    left: 130px; top: 560px; width: 210px; height: 210px;
    background: radial-gradient(circle, rgba(238,106,85,.26) 0%, rgba(242,234,90,.2) 45%, rgba(244,245,246,0) 70%);
  }
  .burst-right {
    left: 420px; top: 620px; width: 300px; height: 300px;
    background: radial-gradient(circle, rgba(92,198,196,.3) 0%, rgba(243,133,37,.22) 45%, rgba(244,245,246,0) 70%);
  }

  /* headline */
  .headline {
    position: absolute;
    left: 0; top: 0; width: 100%;
    margin: 0;
    font-family: "Bebas Neue", "Oswald", sans-serif;
    font-weight: 400;
  }
  .headline .line {
    position: absolute;
    left: 0; width: 100%;
    text-align: center;
    line-height: 1;
    white-space: nowrap;
  }
  .line.flame {
    font-size: 96px;
    letter-spacing: 3px;
    background: linear-gradient(90deg, var(--flame-1) 0%, var(--flame-1) 45%, var(--flame-2) 100%);
    -webkit-background-clip: text;
    background-clip: text;
    color: transparent;
    -webkit-text-stroke: 2.5px var(--ink);
  }
  .line.plain {
    font-size: 81px;
    color: var(--ink);
    letter-spacing: 2px;
  }
  .l-ignite  { top: 47px; }
  .l-and     { top: 140px; }
  .l-embrace { top: 211px; }
  .l-the     { top: 304px; }
  .l-power   { top: 376px; }
  .l-of      { top: 469px; }
  .l-woman   { top: 541px; }
  .l-with    { top: 633px; }
  .l-mother  { top: 705px; }

  /* brand */
  .brand {
    position: absolute;
    left: 0; width: 100%;
    top: 806px;
    text-align: center;
  }
  .brand-dot {
    display: block;
    width: 30px; height: 30px;
    margin: 0 auto 8px;
    border-radius: 50%;
    background: var(--accent);
  }
  .brand-name {
    font-family: "Barlow", sans-serif;
    font-weight: 600;
    font-size: 30px;
    letter-spacing: 1px;
    color: var(--accent);
    text-transform: uppercase;
  }

  /* event details */
  .details {
    position: absolute;
    left: 0; width: 100%;
    top: 921px;
    text-align: center;
    font-family: "Barlow", sans-serif;
    color: var(--ink);
  }
  .details p { margin: 0; }
  .date { font-size: 20.5px; line-height: 28px; }
  .festival { font-size: 20.5px; line-height: 28px; font-weight: 700; color: var(--accent); }
  .venue { font-size: 20.5px; line-height: 28px; }
  .url { font-size: 20.5px; line-height: 28px; font-weight: 700; margin-top: 10px !important; }
</style>
</head>
<body>
<main class="canvas">
  <article class="poster">
    <div class="deco bunting-left" role="img" aria-label="String of orange and teal festival bunting"></div>
    <div class="deco bunting-right" role="img" aria-label="String of orange and teal festival bunting"></div>
    <div class="deco burst burst-top" role="img" aria-label="Firework burst in coral and violet"></div>
    <div class="deco burst burst-left" role="img" aria-label="Large firework burst in teal, orange and coral"></div>
    <div class="deco burst burst-mid" role="img" aria-label="Small firework burst in yellow and orange"></div>
    <div class="deco burst burst-low" role="img" aria-label="Firework burst in coral and yellow"></div>
    <div class="deco burst burst-right" role="img" aria-label="Large firework burst in teal, orange and yellow"></div>

    <h1 class="headline">
      <span class="line flame l-ignite">Ignite</span>
      <span class="line plain l-and">And</span>
      <span class="line flame l-embrace">Embrace</span>
      <span class="line plain l-the">The</span>
      <span class="line flame l-power">Power</span>
      <span class="line plain l-of">Of</span>
      <span class="line flame l-woman">Woman</span>
      <span class="line plain l-with">With</span>
      <span class="line flame l-mother">Mother Earth</span>
    </h1>

    <div class="brand">
      <span class="brand-dot"></span>
      <span class="brand-name">Glowing Meadow</span>
    </div>

    <section class="details">
      <p class="date">3–5 July 2020</p>
      <p class="festival">Glowing Meadow Festival</p>
      <p class="venue">Tarlow Campsite, Ashcombe, Fernshire</p>
      <p class="url">www.glowingmeadow.co.uk</p>
    </section>
  </article>
</main>
</body>
</html>
```